Graphic design to illustrate a biblical verse

We are a french organisation based in Quebec (CANADA), sorry for our english spoken.

Design one original template illustration for our web site section : "verset du jour en image" (Illustrated verse of the day)

Here are some examples made internally to give you some guidelines of what we are looking in term of font quality:
-------------------------------

http://www.brivalonette.com/bible/daily-verse/bible-daily-verse.php?day_number=203

http://www.brivalonette.com/bible/daily-verse/bible-daily-verse.php?day_number=50

http://www.brivalonette.com/bible/daily-verse/bible-daily-verse.php?day_number=79

http://www.brivalonette.com/bible/daily-verse/bible-daily-verse.php?day_number=59

http://www.brivalonette.com/bible/daily-verse/bible-daily-verse.php?day_number=149

http://www.brivalonette.com/bible/daily-verse/bible-daily-verse.php?day_number=183

http://www.brivalonette.com/bible/daily-verse/bible-daily-verse.php?day_number=209

http://www.brivalonette.com/bible/daily-verse/bible-daily-verse.php?day_number=220

http://www.brivalonette.com/bible/daily-verse/bible-daily-verse.php?day_number=49

We don't want reproductions of these font models and effects, because we precisely want to see your creativity and your idea.

File caracteristics :
- Illustration size : 1920 x 1080px
- Format : Photoshop .psd

Why the project ?
The template created, will be used as model to create 10 new other illustations with differents backgrounds, differents biblical verse.

Commitments :
­For all creations, you can use a background illustation corresponded to the verse. We are mainly interested in your creativity for new font style, text effect and all design linked to the text.

The designer must release to us :
- The photoshop source with all text layers editable (very important to replicate it for other illustration!)
- All font files used for the design.

Below is the te verse you must use for the text of your design : (The verse is in french. You don't have to translate. Just use the text as is.)

Jean 14:6 : "Jésus lui dit : Je suis le chemin, la vérité, et la vie. Nul ne vient au Père que par moi"

(Translation in english for your comprehension : John 14:6 : Jesus saith unto him, I am the way, the truth, and the life: no man cometh unto the Father, but by me.)

Thanks you

```html
<!DOCTYPE html>
<html lang="fr">
<head>
<meta charset="utf-8">
<title>Verset du jour — Jean 14:6</title>
<link rel="stylesheet" href="https://fonts.googleapis.com/css2?family=Oswald:wght@300;400&family=Pinyon+Script&display=swap">
<style>
  :root {
    --verse-orange: #e8902a;
    --verse-edge: #8a4a10;
    --panel-veil: rgba(250, 252, 248, 0.55);
    --sky-grey: #66766c;
    --sky-light: #aab8aa;
    --foliage-amber: rgba(200, 140, 50, 0.35);
    --field-green: #7f9a3c;
    --field-deep: #3d5a1e;
  }
  html, body {
    margin: 0;
    padding: 0;
    width: 1200px;
    height: 675px;
    overflow: hidden;
    background: #ffffff;
  }
  .verse-card {
    position: relative;
    width: 1200px;
    height: 675px;
    overflow: hidden;
  }
  .scene-backdrop {
    position: absolute;
    inset: 0;
    background:
      linear-gradient(90deg, rgba(200, 140, 50, 0) 40%, var(--foliage-amber) 100%),
      linear-gradient(180deg, var(--sky-grey) 0%, var(--sky-light) 50%, var(--sky-grey) 70%, var(--field-green) 76%, var(--field-deep) 100%);
  }
  .text-panel {
    position: absolute;
    left: 32px;
    top: 30px;
    width: 582px;
    height: 620px;
    background: var(--panel-veil);
  }
  .verse-text {
    position: absolute;
    left: 32px;
    top: 30px;
    width: 582px;
    margin: 0;
    text-align: center;
    white-space: nowrap;
    font-family: "Oswald", "Arial Narrow", sans-serif;
    font-weight: 400;
    font-size: 76px;
    line-height: 119px;
    letter-spacing: -1.5px;
    color: var(--verse-orange);
    text-shadow: 0 0 1px var(--verse-edge), 1px 1px 0 rgba(138, 74, 16, 0.45);
  }
  .verse-ref, .verse-line { display: block; }
  .swash {
    font-family: "Pinyon Script", cursive;
    font-size: 1.15em;
    line-height: 0;
    font-weight: 400;
    letter-spacing: 0;
  }
</style>
</head>
<body>
  <main class="verse-card">
    <div class="scene-backdrop" role="img" aria-label="Arbre aux feuilles dorées dans une prairie verte sous un ciel nuageux, avec des feuilles qui volent au vent"></div>
    <div class="text-panel"></div>
    <h1 class="verse-text">
      <span class="verse-ref"><span class="swash">J</span>ean 14:6 :</span>
      <span class="verse-line">"<span class="swash">J</span>ésus lui dit : <span class="swash">J</span>e suis</span>
      <span class="verse-line">le chemin, la vérité, et</span>
      <span class="verse-line">la vie. <span class="swash">N</span>ul ne vient au</span>
      <span class="verse-line"><span class="swash">P</span>ère que par moi"</span>
    </h1>
  </main>
</body>
</html>
```